Patent Law

Need to develop a home page for a patent lawyer.

Colors should go with logo, blues...

Company Name- Corvel Tindry, PLLC

Company Overview-

I am an Intellectual Property Lawyer and focus on patents, copyrights, trademarks, & trade secrets. I work with small businesses and start ups in the chemical and biotech industries.

Why Us-

I am small firm that can provide large-firm service at a reasonable price. I also can charge flat-fees for entreprenuers in certain practice areas.

Services-
Intellectual Property
Patents
Copyrights
Trademarks
Trade secrets
Healthcare Compliance
Elder law
Wills
Trusts

Website we like-
http://www.quarnlowtide.example/ - within industry!!
http://www.vopperhask.example/
http://dulbrickovan.example/
http://thefernwoldguides.example/

Target Market(s)

My customers will be small business, specifically small start-up companies in the chemical and biotech arena.

Industry/Entity Type

Trade

Requirements
Must have
• Colors should go with logo, blues...

```html
<!DOCTYPE html>
<html lang="en">
<head>
<meta charset="utf-8">
<title>Corvel Tindry, PLLC — Intellectual Property Law</title>
<link href="https://fonts.googleapis.com/css2?family=Open+Sans:wght@400;600;700&family=PT+Sans:wght@400;700&family=PT+Sans+Narrow&display=swap" rel="stylesheet">
<style>
:root{
  --blue:#0d5aae;
  --blue-dark:#0a4d98;
  --blue-bright:#1b7fc4;
  --navy:#1d2a3a;
  --grey-text:#555;
  --light:#f1f1f1;
  --band:#dcdcdc;
  --white:#fff;
}
*{box-sizing:border-box;margin:0;padding:0}
html,body{width:957px;height:1200px;overflow:hidden}
body{font-family:"PT Sans",sans-serif;background:var(--white);position:relative;color:var(--navy)}
.site-header{position:absolute;left:0;top:0;width:957px;height:133px;background:linear-gradient(#fff,#eee)}
.brand{position:absolute;left:12px;top:86px;display:flex;align-items:center;gap:8px;font-family:"Open Sans",sans-serif;font-weight:600;font-size:25px;color:var(--navy);letter-spacing:1px;text-transform:uppercase}
.brand-mark{width:16px;height:16px;border-radius:50%;background:var(--blue)}
.call{position:absolute;right:14px;top:16px;font-family:"Open Sans",sans-serif;font-weight:700;font-size:25px;color:#555}
.call b{color:var(--blue-bright)}
.social{display:flex;gap:8px}
.header-social{position:absolute;left:630px;top:57px}
.social span{width:25px;height:25px;border-radius:4px;background:#9aa7b3;display:block}
.social .mail{background:#dfe6ec;border:1px solid #b8c3cc;position:relative}
.social .mail svg{position:absolute;left:3px;top:5px}
.search{position:absolute;left:770px;top:57px;width:175px;height:24px;border:1px solid #ccc;background:#fff}
.main-nav{position:absolute;right:10px;top:98px;display:flex;font-family:"Open Sans",sans-serif;font-weight:600;font-size:15px}
.main-nav a{color:var(--navy);text-decoration:none;padding:0 12px;border-left:2px solid var(--navy);line-height:20px}
.main-nav a:first-child{border-left:none}
.hero{position:absolute;left:0;top:133px;width:957px;height:371px;background:linear-gradient(90deg,#f4f4f6 0%,#eceef2 45%,#c7cdd6 70%,#5a5e68 100%)}
.welcome{position:absolute;left:0;top:504px;width:957px;height:130px;background:var(--blue);color:#fff;text-align:center}
.welcome h1{font-family:"Open Sans",sans-serif;font-weight:400;font-size:33px;margin-top:26px}
.welcome p{font-family:"Open Sans",sans-serif;font-size:12px;line-height:17px;margin:4px auto 0;width:740px}
.features{position:absolute;left:0;top:636px;width:957px;height:357px;background:#e4e4e4}
.card{position:absolute;top:56px;width:206px;height:268px;background:var(--blue);color:#fff;padding:78px 16px 0;box-shadow:0 2px 5px rgba(0,0,0,.25)}
.card h2{font-family:"Open Sans",sans-serif;font-weight:700;font-size:18px;text-align:center;margin-bottom:12px}
.card p,.card li{font-family:"Open Sans",sans-serif;font-size:11.5px;line-height:14.5px;list-style:none}
.card-photo{position:absolute;left:50%;top:-40px;transform:translateX(-50%);width:104px;height:104px;border-radius:50%;border:3px solid #fff}
.band{position:absolute;left:0;top:993px;width:957px;height:101px;background:var(--band)}
.band .brand{top:40px;left:40px;font-size:22px}
.band-arrow{position:absolute;left:375px;top:31px}
.help{position:absolute;left:468px;top:24px;font-family:"Open Sans",sans-serif;color:#555;font-size:17px}
.help strong{display:block;color:var(--blue-bright);font-size:29px;line-height:34px}
.divider{position:absolute;left:729px;top:17px;width:1px;height:70px;background:#888}
.connect{position:absolute;left:751px;top:24px;font-family:"Open Sans",sans-serif;color:#555;font-size:17px}
.connect .social{margin-top:10px;margin-left:6px;gap:11px}
.site-footer{position:absolute;left:0;top:1094px;width:957px;height:106px;background:var(--blue)}
.footer-nav{position:absolute;left:60px;top:38px;display:flex;gap:26px;font-family:"Open Sans",sans-serif;font-size:13px}
.footer-nav a{color:#fff;text-decoration:none}
.copyright{position:absolute;left:60px;top:60px;font-size:11.5px;color:#dfe9f6}
.newsletter{position:absolute;left:640px;top:22px;color:#fff}
.newsletter h3{font-family:"PT Sans Narrow",sans-serif;font-weight:400;font-size:19px;margin-bottom:8px}
.newsletter input{width:186px;height:26px;border:none;padding:0 7px;font-size:12px;vertical-align:top}
.newsletter button{height:26px;margin-left:4px;padding:0 12px;border:none;background:#444;color:#fff;font-size:12px}
</style>
</head>
<body>
<header class="site-header">
  <div class="brand"><span class="brand-mark"></span>Corvel Tindry, PLLC</div>
  <div class="call"><b>Call</b> (555) 014-2287</div>
  <div class="social header-social">
    <span class="mail"><svg width="17" height="13" viewBox="0 0 17 13"><rect x=".5" y=".5" width="16" height="12" fill="#fff" stroke="#7a8896"/><path d="M.5 .5 8.5 7 16.5 .5" fill="none" stroke="#7a8896"/></svg></span>
    <span></span><span></span><span></span>
  </div>
  <div class="search"></div>
  <nav class="main-nav">
    <a href="#">Home</a><a href="#">Firm Overview</a><a href="#">Why Us</a><a href="#">Services</a><a href="#">Resources</a><a href="#">Contact Us</a>
  </nav>
</header>

<section class="hero" role="img" aria-label="Intellectual property cycle diagram (protection, successful business, creation, application) touched by a hand, beside two smiling business professionals"></section>

<section class="welcome">
  <h1>Welcome to Corvel Tindry, PLLC</h1>
  <p>I am an Intellectual Property Lawyer and focus on patents, copyrights, trademarks, &amp; trade secrets. I work with small businesses and start ups in the chemical and biotech industries.</p>
</section>

<section class="features">
  <article class="card" style="left:47px">
    <div class="card-photo" role="img" aria-label="Business handshake photo" style="background:radial-gradient(#e9e9ec,#b7bcc4)"></div>
    <h2>WHY CORVEL TINDRY</h2>
    <p>I am an Intellectual Property Lawyer and focus on patents, copyrights, trademarks, &amp; trade secrets. I work with small businesses and start ups in the chemical and biotech industries.</p>
  </article>
  <article class="card" style="left:262px">
    <div class="card-photo" role="img" aria-label="Judge's gavel photo" style="background:radial-gradient(#f2efec,#8a5a36)"></div>
    <h2>WHAT WE DO</h2>
    <ul><li>Intellectual Property</li><li>Patents</li><li>Copyrights</li><li>Trademarks</li><li>Trade secrets</li><li>Healthcare Compliance</li><li>Elder law</li><li>Wills</li><li>Trusts</li></ul>
  </article>
  <article class="card" style="left:477px">
    <div class="card-photo" role="img" aria-label="Press microphones photo" style="background:radial-gradient(#6aa7dc,#0c2a4c)"></div>
    <h2>NEWS</h2>
    <p>I am an Intellectual Property Lawyer and focus on patents, copyrights, trademarks, &amp; trade secrets. I work with small businesses and start ups in the chemical and biotech industries.</p>
  </article>
  <article class="card" style="left:691px">
    <div class="card-photo" role="img" aria-label="Support agent with headset photo" style="background:radial-gradient(#f3f3f3,#c4b7ab)"></div>
    <h2>CONTACT INFO</h2>
    <p>4120 Larkmoor Bend, Brindlecove, Westmarch-30482, Eldoria.<br>Phone : (555) 014-2287<br>Email : info@corveltindry.example</p>
  </article>
</section>

<section class="band">
  <div class="brand"><span class="brand-mark"></span>Corvel Tindry, PLLC</div>
  <svg class="band-arrow" width="66" height="44" viewBox="0 0 66 44"><path d="M1 14H40V2L64 22 40 42V30H1Z" fill="#f4f4f4" stroke="#888" stroke-width="1.5"/></svg>
  <div class="help">New Help Planning? Call us!<strong>(555) 014-2287</strong></div>
  <div class="divider"></div>
  <div class="connect">Connect with us on
    <div class="social">
      <span class="mail"><svg width="17" height="13" viewBox="0 0 17 13"><rect x=".5" y=".5" width="16" height="12" fill="#fff" stroke="#7a8896"/><path d="M.5 .5 8.5 7 16.5 .5" fill="none" stroke="#7a8896"/></svg></span>
      <span></span><span></span><span></span>
    </div>
  </div>
</section>

<footer class="site-footer">
  <nav class="footer-nav">
    <a href="#">Home</a><a href="#">Firm Overview</a><a href="#">Why Us</a><a href="#">Services</a><a href="#">Resources</a><a href="#">Contact Us</a>
  </nav>
  <p class="copyright">Copyright (c)2013 by Corvel Tindry, PLLC</p>
  <form class="newsletter">
    <h3>Subscribe to our Newsletter</h3>
    <input type="email" placeholder="Your Email Address"><button type="button">Submit</button>
  </form>
</footer>
</body>
</html>
```